Zertifikat-Design und Garantieschein-Design für Uhrenmanufaktur gesucht
Zielgruppe
Wir sind eine Uhrenmanufaktur und fertigen hochwertige mechanische Armbanduhren in größten Teilen in Handarbeit.
Für die Auslieferung unserer Uhren brauchen wir ein Zertifikat und einen Garantieschein (jeweils 1 Blatt).
Unsere Zielgruppe sind gutverdienende Menschen zwischen 25 und 55 Jahren.
Aufgabenstellung
Es soll jeweils ein Zertifikat erstellt werden (1 Blatt - nur Vorderseite) und ein Garantieschein (1 Blatt - Vorder- und Rückseite). Alle Vorgaben, sowie Bilder der Uhren als Inspiration sind in der PDF enthalten.

```html
<!DOCTYPE html>
<html lang="de">
<head>
<meta charset="utf-8">
<title>HALDEN Zertifikat</title>
<link rel="stylesheet" href="https://fonts.googleapis.com/css2?family=Jost:wght@300;400;500&display=swap">
<style>
  :root {
    --page-bg: #e9e7e5;
    --frame: #80b6b4;
    --panel: #deeeed;
    --ink: #1e1e1e;
    --accent: #2a6576;
    --rule: #2f6e78;
    --field-line: #93bdbd;
    --seal: #eef3f3;
  }
  * { margin: 0; padding: 0; box-sizing: border-box; }
  html, body { width: 1200px; height: 1188px; overflow: hidden; }
  body { background: var(--page-bg); font-family: "Jost", sans-serif; color: var(--ink); position: relative; }

  .sheet { position: absolute; left: 175px; top: 34px; width: 850px; height: 1117px; background: var(--frame); }
  .panel { position: absolute; left: 31px; top: 28px; width: 790px; height: 1055px; background: var(--panel); }
  .abs { position: absolute; white-space: nowrap; }

  .brand { left: 0; width: 850px; text-align: center; top: 112px; font-size: 88px; font-weight: 300; letter-spacing: 2px; line-height: 100px; }
  .brand-sub { left: 0; width: 850px; text-align: center; top: 212px; font-size: 34px; font-weight: 400; letter-spacing: 3px; line-height: 40px; }
  .title { left: 0; width: 850px; text-align: center; top: 272px; font-size: 56px; font-weight: 400; letter-spacing: 3px; line-height: 64px; }
  .title .slash { color: var(--accent); }

  .label { font-size: 14px; line-height: 20px; }
  .label b { font-weight: 500; }
  .section { font-size: 14px; line-height: 21px; color: var(--accent); }
  .section b { font-weight: 500; }
  .line { position: absolute; height: 1px; background: var(--field-line); }
  .rule { position: absolute; left: 80px; width: 692px; height: 1.5px; background: var(--rule); }
  .statement { left: 80px; top: 499px; font-size: 14px; line-height: 21px; color: var(--accent); }
  .statement b { font-weight: 500; }

  .date { left: 80px; top: 990px; font-size: 14px; line-height: 20px; }
  .caption { font-size: 11px; line-height: 14px; color: var(--accent); }
  .caption b { font-weight: 500; }
  .signature-area { position: absolute; left: 299px; top: 950px; width: 328px; height: 60px; background: #d3e6e5; }
  .seal { position: absolute; left: 650px; top: 933px; }
</style>
</head>
<body>
<div class="sheet">
  <div class="panel"></div>

  <div class="abs brand">HALDEN</div>
  <div class="abs brand-sub">UHRMACHER</div>
  <div class="abs title">ZERTIFIKAT <span class="slash">/</span> CERTIFICATE</div>

  <!-- Model data -->
  <div class="abs label" style="left:80px;top:400px"><b>Modellname</b> / Model name:</div>
  <div class="abs label" style="left:80px;top:421px"><b>Referenznr.</b> / Reference No.:</div>
  <div class="abs label" style="left:80px;top:441px"><b>Kaliber</b> / Caliber:</div>
  <div class="line" style="left:356px;width:416px;top:414px"></div>
  <div class="line" style="left:356px;width:416px;top:435px"></div>
  <div class="line" style="left:356px;width:416px;top:455px"></div>

  <div class="rule" style="top:491px"></div>
  <div class="abs statement"><b>Diese Uhr wurde hergestellt, montiert und einreguliert im HALDEN-Atelier in Dresden. /</b><br>This watch was made, assembled and adjusted in the HALDEN atelier in Dresden, Germany.</div>
  <div class="rule" style="top:547px"></div>

  <!-- Specifications -->
  <div class="abs section" style="left:80px;top:579px"><b>Spezifikationen /</b><br>Specifications</div>
  <div class="abs label" style="left:221px;top:579px"><b>Gehäuse</b> / Case:</div>
  <div class="abs label" style="left:221px;top:599px"><b>Glas</b> / Glass:</div>
  <div class="abs label" style="left:221px;top:620px"><b>Band</b> / Strap:</div>
  <div class="abs label" style="left:221px;top:640px"><b>Schließe</b> / Buckle:</div>
  <div class="abs label" style="left:221px;top:661px"><b>Zeiger</b> / Hands:</div>
  <div class="abs label" style="left:221px;top:681px"><b>Zifferblatt</b> / Dial:</div>
  <div class="line" style="left:356px;width:414px;top:596px"></div>
  <div class="line" style="left:356px;width:414px;top:616px"></div>
  <div class="line" style="left:356px;width:414px;top:637px"></div>
  <div class="line" style="left:356px;width:414px;top:657px"></div>
  <div class="line" style="left:356px;width:414px;top:678px"></div>
  <div class="line" style="left:356px;width:414px;top:698px"></div>

  <!-- Purchaser -->
  <div class="abs section" style="left:82px;top:765px"><b>Käufer /</b><br>Purchaser</div>
  <div class="abs label" style="left:221px;top:765px"><b>Name</b> / Name:</div>
  <div class="abs label" style="left:221px;top:786px"><b>Straße</b> / Street:</div>
  <div class="abs label" style="left:221px;top:807px"><b>Stadt</b> / City:</div>
  <div class="abs label" style="left:648px;top:786px"><b>PLZ</b> / Zip:</div>
  <div class="abs label" style="left:648px;top:807px"><b>Land</b> / Land:</div>
  <div class="line" style="left:356px;width:414px;top:781px"></div>
  <div class="line" style="left:356px;width:414px;top:802px"></div>
  <div class="line" style="left:356px;width:414px;top:823px"></div>

  <!-- Seller -->
  <div class="abs section" style="left:80px;top:849px"><b>Veräufer /</b><br>Seller</div>
  <div class="abs label" style="left:221px;top:849px"><b>Name</b> / Name:</div>
  <div class="abs label" style="left:221px;top:870px"><b>Straße</b> / Street:</div>
  <div class="abs label" style="left:221px;top:891px"><b>Stadt</b> / City:</div>
  <div class="abs label" style="left:648px;top:870px"><b>PLZ</b> / Zip:</div>
  <div class="abs label" style="left:648px;top:891px"><b>Land</b> / Land:</div>
  <div class="line" style="left:356px;width:414px;top:865px"></div>
  <div class="line" style="left:356px;width:414px;top:886px"></div>
  <div class="line" style="left:356px;width:414px;top:907px"></div>

  <!-- Footer -->
  <div class="abs date">01. August 2022</div>
  <div class="line" style="left:80px;width:184px;top:1017px;background:var(--rule)"></div>
  <div class="abs caption" style="left:80px;top:1025px"><b>Ausstellungsdatum</b> / Date of issue</div>

  <div class="signature-area" role="img" aria-label="Handgeschriebene Unterschrift"></div>
  <div class="line" style="left:299px;width:328px;top:1017px;background:var(--rule)"></div>
  <div class="abs caption" style="left:299px;top:1025px"><b>Unterschrift</b> / Sign</div>

  <svg class="seal" width="124" height="124" viewBox="0 0 124 124" aria-hidden="true">
    <circle cx="62" cy="62" r="60" fill="var(--seal)" stroke="#ffffff" stroke-width="3"/>
  </svg>
</div>
</body>
</html>
```